Travel Activities - Tours, sightseeing tours, activities & things to do website design

We need a web design that covers Tours, sightseeing tours, activities and things to do in the travel industry. Need to be a simple design with good SEO technical structure and conversion optimised design.
Inspirations
Similar site - https://www.roamlyx.com/London/d512-qzp?pub=KTW8RN_4_7
Design and layout - https://www.stayburo.com.au/europe-264/hotel
Colours - please suggest ( prefer happy energetic colours )
Pages
1. Home page design
2. Individual tour or activity page design
Target Market(s)
Independent travellers who want to plan the holiday by themselfs.
Industry/Entity Type
Travel Industry
Number of Pages Required
2 page
Font styles to use
Colors
Designer to choose colors to be used in the design.
Requirements
Must have
- Pages
- 1. Home page design
- 2. Individual tour or activity page design
- SEO
- H1 tags
- Text Descriptions
- Internal linking to other tours activities

```html
<!DOCTYPE html>
<html lang="en">
<head>
<meta charset="utf-8">
<title>Tours, Tickets, Activities &amp; Things To Do in London | Tripwell Finder</title>
<link href="https://fonts.googleapis.com/css2?family=Roboto:wght@400;500;700;900&display=swap" rel="stylesheet">
<style>
:root{
  --blue:#2f80cc;
  --blue-dark:#2a6fb4;
  --blue-deep:#2469ad;
  --orange:#ff8a00;
  --text:#333;
  --muted:#777;
  --line:#dcdcdc;
  --price:#2f80cc;
  --star:#f5a623;
  --heart:#e8262a;
  --white:#fff;
}
*{box-sizing:border-box;margin:0;padding:0}
html,body{width:1200px;height:3529px;overflow:hidden}
body{font-family:'Roboto',Arial,sans-serif;color:var(--text);background:var(--white);position:relative;font-size:14px}
a{color:inherit;text-decoration:none}
svg{display:inline-block;vertical-align:middle}

/* header */
.site-header{position:absolute;left:0;top:0;width:1200px;height:212px;background:var(--blue)}
.topbar{height:33px;background:var(--blue-dark);color:#fff;font-size:12px;font-weight:500;display:flex;align-items:center;justify-content:space-between;padding:0 0 0 99px}
.topbar .group{display:flex;align-items:center;gap:26px;height:100%}
.topbar .item{display:flex;align-items:center;gap:6px}
.topbar .cart{background:var(--orange);height:100%;padding:0 24px;margin-right:99px}
.brand{position:absolute;left:99px;top:60px;color:#fff;font-size:23px;font-weight:700;letter-spacing:.3px}
.search{position:absolute;left:619px;top:52px;display:flex;height:42px}
.search .field{width:386px;background:#fff;display:flex;align-items:center;padding-left:14px}
.search .btn{width:96px;background:var(--blue-deep);color:#fff;font-weight:700;font-size:14px;display:flex;align-items:center;justify-content:center}
.header-rule{position:absolute;left:99px;top:113px;width:1002px;height:1px;background:rgba(255,255,255,.45)}
.loc{position:absolute;top:134px;height:47px;border:1px solid rgba(255,255,255,.6);color:#fff;font-size:14px;display:flex;align-items:center;gap:8px;padding-left:16px}
.loc.country{left:190px;width:365px}
.loc.city{left:595px;width:337px}
.go{position:absolute;left:944px;top:134px;width:68px;height:47px;background:var(--orange);color:#fff;font-weight:700;font-size:16px;display:flex;align-items:center;justify-content:center;border-radius:3px}

/* breadcrumb */
.crumbs{position:absolute;left:99px;top:222px;font-size:13px;font-weight:700}
.crumbs .current{color:var(--orange)}
.share{position:absolute;right:99px;top:220px;display:flex;gap:10px;align-items:center;font-size:10px;color:#888}
.share .btn{height:20px;padding:0 8px;color:#fff;font-weight:700;display:flex;align-items:center;border-radius:2px}
.share .b1{background:#3b5998}.share .b2{background:#1da1f2}.share .b3{background:#dd4b39;width:26px}
.crumb-rule{position:absolute;left:99px;top:259px;width:1002px;height:2px;background:#ccc}

/* sidebar */
.sidebar{position:absolute;left:99px;top:301px;width:207px}
.filter-head{height:38px;background:var(--orange);color:#fff;font-weight:700;font-size:17px;display:flex;align-items:center;justify-content:space-between;padding:0 14px}
.filter-head.blue{background:var(--blue);margin-top:26px}
.tours-panel{border:1px solid var(--line);border-top:none;padding:12px 10px 18px}
.tours-panel .label{font-size:14px;margin-bottom:10px}
.date{height:32px;border:1px solid #ccc;display:flex;align-items:center;justify-content:space-between;padding:0 10px;color:#999;font-size:13px;margin-top:8px}
.newsletter{margin-top:72px;border:2px solid #ddd;padding:14px 12px 20px;height:174px}
.newsletter h3{font-size:18px;font-weight:900;margin-bottom:14px}
.newsletter .email{height:34px;border:1px solid #bbb;font-size:13px;display:flex;align-items:center;padding-left:12px;width:180px;margin-bottom:12px}
.newsletter .signup{display:inline-block;background:var(--orange);color:#fff;font-weight:700;font-size:13px;padding:10px 18px;border-radius:4px}

/* main */
.main{position:absolute;left:346px;top:299px;width:755px}
.hero{height:183px;background:linear-gradient(180deg,#5a7fa6 0%,#2c4a6a 55%,#1e3247 100%);position:relative}
.hero h1{position:absolute;left:34px;top:68px;color:#fff;font-size:31px;font-weight:700}
.intro{margin-top:30px;font-size:13.5px;line-height:24px;color:#777}
.read-more{margin-top:14px;color:var(--orange);font-weight:700;font-size:13px}
.toolbar{margin-top:40px;height:44px;display:flex;justify-content:space-between;align-items:center;border-bottom:2px solid #ccc;padding-bottom:10px;height:54px}
.toolbar .count{font-size:15px}
.sort{display:flex;align-items:center;gap:14px;font-size:13px;font-weight:700}
.sort .select{width:178px;height:40px;border:1px solid #ccc;display:flex;align-items:center;justify-content:space-between;padding-left:14px;font-weight:400;color:#666}
.sort .select span.arrow{border-left:1px solid #ccc;height:100%;width:36px;display:flex;align-items:center;justify-content:center}

.grid{margin-top:43px;display:grid;grid-template-columns:repeat(3,242px);column-gap:14.5px;row-gap:35px}
.card{height:426px;border:1px solid #ddd;box-shadow:0 1px 4px rgba(0,0,0,.12);background:#fff}
.card .photo{height:172px;position:relative}
.card .heart{position:absolute;right:10px;bottom:8px}
.card .body{padding:14px 14px 0}
.card h2{font-size:15px;font-weight:700;line-height:21px}
.rating{margin-top:8px;font-size:13px;color:#555;display:flex;align-items:center;gap:4px}
.meta{margin-top:8px;font-size:13px;color:#555;display:flex;align-items:center;gap:6px}
.card hr{border:none;border-top:1px solid #ccc;margin:14px 0 16px}
.pick{font-size:14px}
.from{font-size:14px;margin-top:4px}
.from b{color:var(--price);font-size:22px;font-weight:700}
.deal{display:inline-block;margin-top:14px;border:1px solid #999;border-radius:4px;color:var(--orange);font-weight:700;font-size:13px;padding:9px 14px}

.pager{position:absolute;top:1951px;left:0;display:flex;gap:6px;font-size:11px}
.pager span{height:24px;min-width:24px;padding:0 7px;border:1px solid #ccc;display:flex;align-items:center;justify-content:center;box-shadow:0 1px 2px rgba(0,0,0,.1)}
.pager .on{background:var(--orange);color:#fff;border-color:var(--orange)}

.panel{position:absolute;left:0;width:755px;background:#fff;border:1px solid #e2e2e2;box-shadow:0 1px 5px rgba(0,0,0,.12)}
.destinations{top:2031px;height:364px}
.destinations h2{position:absolute;left:28px;top:30px;font-size:32px;font-weight:700}
.arrows{position:absolute;right:26px;top:40px;display:flex;gap:4px}
.dest-row{position:absolute;left:28px;top:99px;display:flex;gap:22px}
.dest{width:219px;height:225px;border:1px solid #ddd;box-shadow:0 1px 3px rgba(0,0,0,.12)}
.dest .photo{height:158px}
.dest .info{padding:12px 14px;display:flex;justify-content:space-between}
.dest .name{font-weight:700;font-size:16px}
.dest .sub{font-style:italic;font-size:13px;color:#666;margin-top:3px}
.dest .price{color:var(--orange);font-weight:700;font-size:16px}
.things{top:2438px;height:336px}
.things h2{position:absolute;left:38px;top:30px;font-size:32px;font-weight:700}
.things ul{position:absolute;top:98px;list-style:none;font-size:14px;color:#555}
.things li{height:29px;display:flex;align-items:center;gap:10px}
.things li::before{content:"";width:12px;height:12px;border-radius:50%;background:var(--orange);box-shadow:inset 0 0 0 3px var(--orange)}

/* footer */
.site-footer{position:absolute;left:0;top:3153px;width:1200px;height:376px;background:var(--blue);color:#fff}
.site-footer .logo{position:absolute;left:94px;top:108px;font-size:25px;font-weight:700}
.site-footer .about{position:absolute;left:94px;top:155px;width:290px;font-size:13px;line-height:22px}
.socials{position:absolute;left:94px;top:220px;display:flex;gap:9px}
.socials span{width:26px;height:26px;border-radius:50%;background:rgba(255,255,255,.9)}
.fcol{position:absolute;top:80px;font-size:12.5px}
.fcol h4{font-size:17px;font-weight:700;margin-bottom:16px}
.fcol li{list-style:none;height:29px}
.fcol.c1{left:468px}.fcol.c2{left:670px}.fcol.c3{left:920px}
.fsep{position:absolute;top:80px;width:1px;height:160px;background:rgba(255,255,255,.3)}
.copyright{position:absolute;left:0;right:0;top:306px;border-top:1px solid rgba(255,255,255,.3);text-align:center;padding-top:26px;font-size:12px;margin:0 94px}
</style>
</head>
<body>

<header class="site-header">
  <div class="topbar">
    <div class="group">
      <span class="item">USD ($) <svg width="8" height="5"><path d="M0 0h8L4 5z" fill="#fff"/></svg></span>
      <span class="item"><svg width="16" height="10"><rect width="16" height="10" fill="#e9eef7"/><rect y="4" width="16" height="2" fill="#c8102e"/><rect x="7" width="2" height="10" fill="#c8102e"/></svg> ENGLISH</span>
      <span class="item"><svg width="12" height="12"><circle cx="6" cy="6" r="6" fill="#fff"/><text x="6" y="9.5" font-size="9" text-anchor="middle" fill="#2a6fb4" font-weight="700" font-family="Roboto">?</text></svg> HELP</span>
    </div>
    <div class="group">
      <span class="item"><svg width="12" height="12"><rect x="0" y="2" width="12" height="10" fill="#fff"/><rect x="1.5" y="5" width="9" height="5.5" fill="#2a6fb4"/></svg> MANAGE MY BOOKING</span>
      <span class="item"><svg width="12" height="12"><circle cx="6" cy="3.5" r="3" fill="#fff"/><path d="M0 12a6 5 0 0 1 12 0z" fill="#fff"/></svg> LOG IN / REGISTER</span>
      <span class="item cart"><svg width="13" height="12"><path d="M0 1h3l2 7h7l1-5H4" stroke="#fff" fill="none" stroke-width="1.5"/><circle cx="6" cy="10.5" r="1.3" fill="#fff"/><circle cx="11" cy="10.5" r="1.3" fill="#fff"/></svg> CART (0)</span>
    </div>
  </div>
  <div class="brand">TRIPWELL FINDER</div>
  <div class="search">
    <div class="field"><svg width="16" height="16"><circle cx="6.5" cy="6.5" r="5" stroke="#555" stroke-width="2" fill="none"/><path d="M10 10l5 5" stroke="#555" stroke-width="2"/></svg></div>
    <div class="btn">SEARCH</div>
  </div>
  <div class="header-rule"></div>
  <div class="loc country"><svg width="10" height="14"><path d="M5 0a5 5 0 0 1 5 5c0 4-5 9-5 9S0 9 0 5a5 5 0 0 1 5-5z" fill="#fff"/><circle cx="5" cy="5" r="2" fill="#2f80cc"/></svg> England</div>
  <div class="loc city"><svg width="10" height="14"><path d="M5 0a5 5 0 0 1 5 5c0 4-5 9-5 9S0 9 0 5a5 5 0 0 1 5-5z" fill="#fff"/><circle cx="5" cy="5" r="2" fill="#2f80cc"/></svg> London</div>
  <div class="go">GO</div>
</header>

<nav class="crumbs">HOME › ENGLAND › <span class="current">LONDON</span></nav>
<div class="share"><span class="btn b1">Share</span>0 <span class="btn b2">Tweet</span>1 <span class="btn b3"></span>+1</div>
<div class="crumb-rule"></div>

<aside class="sidebar">
  <div class="filter-head">TOURS <svg width="12" height="8"><path d="M1 7l5-5 5 5" stroke="#fff" stroke-width="2" fill="none"/></svg></div>
  <div class="tours-panel">
    <div class="label">Travel Dates</div>
    <div class="date">From <svg width="13" height="13"><rect x=".5" y="2" width="12" height="10.5" fill="none" stroke="#666"/><rect x=".5" y="2" width="12" height="3" fill="#666"/></svg></div>
    <div class="date">To <svg width="13" height="13"><rect x=".5" y="2" width="12" height="10.5" fill="none" stroke="#666"/><rect x=".5" y="2" width="12" height="3" fill="#666"/></svg></div>
  </div>
  <div class="filter-head blue" style="margin-top:38px">CATEGORIES <svg width="12" height="8"><path d="M1 1l5 5 5-5" stroke="#fff" stroke-width="2" fill="none"/></svg></div>
  <div class="filter-head blue">SPECIALS <svg width="12" height="8"><path d="M1 1l5 5 5-5" stroke="#fff" stroke-width="2" fill="none"/></svg></div>
  <div class="filter-head blue" style="margin-top:24px">PRICE RANGE <svg width="12" height="8"><path d="M1 1l5 5 5-5" stroke="#fff" stroke-width="2" fill="none"/></svg></div>
  <div class="filter-head blue" style="margin-top:24px">DURATION <svg width="12" height="8"><path d="M1 1l5 5 5-5" stroke="#fff" stroke-width="2" fill="none"/></svg></div>
  <div class="newsletter" style="margin-top:30px">
    <h3>NEWSLETTER SIGN UP</h3>
    <div class="email">Email Address</div>
    <span class="signup">SIGN UP</span>
  </div>
</aside>

<main class="main">
  <section class="hero" role="img" aria-label="London skyline with Tower Bridge over the Thames at dusk">
    <h1>Tours, Tickets, Activities &amp; Things To Do</h1>
  </section>
  <p class="intro">Sed ut perspiciatis unde omnis iste natus error sit voluptatem accusantium doloremque laudantium, totam rem aperiam, eaque ipsa quae ab illo inventore veritatis et quasi architecto beatae vitae dicta sunt explicabo. Nemo enim ipsamvolup tatem quia voluptas sit aspernatur aut odit aut fugit, sed quia consequuntur magni dolores eos qui ratione voluptatem sequi nesciunt. Neque porro quisquam est, qui dolorem ipsum quia dolor sit amet, consectetur, adipisci velit, sed quia non numquam eius modi tempora incidunt ut labore et dolore magnam aliquam quaerat voluptatem. Ut enim ad mini ma veniam, quis nostrum exercitationem ullam corporis suscipit.</p>
  <div class="read-more">READ MORE &gt;&gt;</div>
  <div class="toolbar">
    <span class="count">626 out of 1,099,949 hotels</span>
    <div class="sort">SORT BY: <div class="select">Most Popular <span class="arrow"><svg width="10" height="6"><path d="M0 0h10L5 6z" fill="#888"/></svg></span></div></div>
  </div>

  <div class="grid">
    <!-- card template repeated -->
    <article class="card"><div class="photo" role="img" aria-label="Hotel with pool and palm trees" style="background:linear-gradient(180deg,#7fb6e6,#d9c9a5 55%,#2aa3c9)"><svg class="heart" width="20" height="18"><path d="M10 17S0 10.5 0 5a5 5 0 0 1 10-1 5 5 0 0 1 10 1c0 5.5-10 12-10 12z" fill="#e8262a"/></svg></div><div class="body"><h2>Stonehenge, Windsor Castle, and Bath from London..</h2><div class="rating"><svg width="64" height="12"><g fill="#f5a623"><path id="s" d="M6 0l1.8 3.9 4.2.5-3.1 2.9.8 4.2L6 9.4 2.3 11.5l.8-4.2L0 4.4l4.2-.5z"/><use href="#s" x="13"/><use href="#s" x="26"/><use href="#s" x="39"/><use href="#s" x="52"/></g></svg> 5042 Reviews</div><div class="meta"><svg width="9" height="12"><path d="M4.5 0a4.5 4.5 0 0 1 4.5 4.5C9 8 4.5 12 4.5 12S0 8 0 4.5A4.5 4.5 0 0 1 4.5 0z" fill="#ff8a00"/></svg> London, UK | <svg width="12" height="12"><circle cx="6" cy="6" r="5" fill="none" stroke="#ff8a00" stroke-width="1.6"/><path d="M6 3v3h2" stroke="#ff8a00" stroke-width="1.4" fill="none"/></svg> 11 hours</div><hr><div class="pick">Top Insider's Pick</div><div class="from">From USD <b>$136.83</b></div><span class="deal">VIEW DEAL</span></div></article>

    <article class="card"><div class="photo" role="img" aria-label="Lakeside palace among trees" style="background:linear-gradient(180deg,#4f8fd6,#8aa6a0 50%,#3b5e4a)"><svg class="heart" width="20" height="18"><path d="M10 17S0 10.5 0 5a5 5 0 0 1 10-1 5 5 0 0 1 10 1c0 5.5-10 12-10 12z" fill="#e8262a"/></svg></div><div class="body"><h2>Stonehenge, Windsor Castle, and Bath from London..</h2><div class="rating"><svg width="64" height="12"><g fill="#f5a623"><use href="#s"/><use href="#s" x="13"/><use href="#s" x="26"/><use href="#s" x="39"/><use href="#s" x="52"/></g></svg> 5042 Reviews</div><div class="meta"><svg width="9" height="12"><path d="M4.5 0a4.5 4.5 0 0 1 4.5 4.5C9 8 4.5 12 4.5 12S0 8 0 4.5A4.5 4.5 0 0 1 4.5 0z" fill="#ff8a00"/></svg> London, UK | <svg width="12" height="12"><circle cx="6" cy="6" r="5" fill="none" stroke="#ff8a00" stroke-width="1.6"/><path d="M6 3v3h2" stroke="#ff8a00" stroke-width="1.4" fill="none"/></svg> 11 hours</div><hr><div class="pick">Top Insider's Pick</div><div class="from">From USD <b>$136.83</b></div><span class="deal">VIEW DEAL</span></div></article>

    <article class="card"><div class="photo" role="img" aria-label="Rooftop pool overlooking a city skyline" style="background:linear-gradient(180deg,#d9a27a,#a98a7a 50%,#7b5a4c)"><svg class="heart" width="20" height="18"><path d="M10 17S0 10.5 0 5a5 5 0 0 1 10-1 5 5 0 0 1 10 1c0 5.5-10 12-10 12z" fill="#e8262a"/></svg></div><div class="body"><h2>Stonehenge, Windsor Castle, and Bath from London..</h2><div class="rating"><svg width="64" height="12"><g fill="#f5a623"><use href="#s"/><use href="#s" x="13"/><use href="#s" x="26"/><use href="#s" x="39"/><use href="#s" x="52"/></g></svg> 5042 Reviews</div><div class="meta"><svg width="9" height="12"><path d="M4.5 0a4.5 4.5 0 0 1 4.5 4.5C9 8 4.5 12 4.5 12S0 8 0 4.5A4.5 4.5 0 0 1 4.5 0z" fill="#ff8a00"/></svg> London, UK | <svg width="12" height="12"><circle cx="6" cy="6" r="5" fill="none" stroke="#ff8a00" stroke-width="1.6"/><path d="M6 3v3h2" stroke="#ff8a00" stroke-width="1.4" fill="none"/></svg> 11 hours</div><hr><div class="pick">Top Insider's Pick</div><div class="from">From USD <b>$136.83</b></div><span class="deal">VIEW DEAL</span></div></article>

    <article class="card"><div class="photo" role="img" aria-label="Waterfront town on a lake" style="background:linear-gradient(180deg,#9fb4c6,#b59a7a 55%,#2f5a78)"><svg class="heart" width="20" height="18"><path d="M10 17S0 10.5 0 5a5 5 0 0 1 10-1 5 5 0 0 1 10 1c0 5.5-10 12-10 12z" fill="#e8262a"/></svg></div><div class="body"><h2>Stonehenge, Windsor Castle, and Bath from London..</h2><div class="rating"><svg width="64" height="12"><g fill="#f5a623"><use href="#s"/><use href="#s" x="13"/><use href="#s" x="26"/><use href="#s" x="39"/><use href="#s" x="52"/></g></svg> 5042 Reviews</div><div class="meta"><svg width="9" height="12"><path d="M4.5 0a4.5 4.5 0 0 1 4.5 4.5C9 8 4.5 12 4.5 12S0 8 0 4.5A4.5 4.5 0 0 1 4.5 0z" fill="#ff8a00"/></svg> London, UK | <svg width="12" height="12"><circle cx="6" cy="6" r="5" fill="none" stroke="#ff8a00" stroke-width="1.6"/><path d="M6 3v3h2" stroke="#ff8a00" stroke-width="1.4" fill="none"/></svg> 11 hours</div><hr><div class="pick">Top Insider's Pick</div><div class="from">From USD <b>$136.83</b></div><span class="deal">VIEW DEAL</span></div></article>

    <article class="card"><div class="photo" role="img" aria-label="Historic lakeside palaces under a blue sky" style="background:linear-gradient(180deg,#2e6fc0,#d4a66a 55%,#1f4f78)"><svg class="heart" width="20" height="18"><path d="M10 17S0 10.5 0 5a5 5 0 0 1 10-1 5 5 0 0 1 10 1c0 5.5-10 12-10 12z" fill="#e8262a"/></svg></div><div class="body"><h2>Stonehenge, Windsor Castle, and Bath from London..</h2><div class="rating"><svg width="64" height="12"><g fill="#f5a623"><use href="#s"/><use href="#s" x="13"/><use href="#s" x="26"/><use href="#s" x="39"/><use href="#s" x="52"/></g></svg> 5042 Reviews</div><div class="meta"><svg width="9" height="12"><path d="M4.5 0a4.5 4.5 0 0 1 4.5 4.5C9 8 4.5 12 4.5 12S0 8 0 4.5A4.5 4.5 0 0 1 4.5 0z" fill="#ff8a00"/></svg> London, UK | <svg width="12" height="12"><circle cx="6" cy="6" r="5" fill="none" stroke="#ff8a00" stroke-width="1.6"/><path d="M6 3v3h2" stroke="#ff8a00" stroke-width="1.4" fill="none"/></svg> 11 hours</div><hr><div class="pick">Top Insider's Pick</div><div class="from">From USD <b>$136.83</b></div><span class="deal">VIEW DEAL</span></div></article>

    <article class="card"><div class="photo" role="img" aria-label="Old stone buildings along the water" style="background:linear-gradient(180deg,#8fb3d9,#c9b08a 50%,#4f7fa0)"><svg class="heart" width="20" height="18"><path d="M10 17S0 10.5 0 5a5 5 0 0 1 10-1 5 5 0 0 1 10 1c0 5.5-10 12-10 12z" fill="#e8262a"/></svg></div><div class="body"><h2>Stonehenge, Windsor Castle, and Bath from London..</h2><div class="rating"><svg width="64" height="12"><g fill="#f5a623"><use href="#s"/><use href="#s" x="13"/><use href="#s" x="26"/><use href="#s" x="39"/><use href="#s" x="52"/></g></svg> 5042 Reviews</div><div class="meta"><svg width="9" height="12"><path d="M4.5 0a4.5 4.5 0 0 1 4.5 4.5C9 8 4.5 12 4.5 12S0 8 0 4.5A4.5 4.5 0 0 1 4.5 0z" fill="#ff8a00"/></svg> London, UK | <svg width="12" height="12"><circle cx="6" cy="6" r="5" fill="none" stroke="#ff8a00" stroke-width="1.6"/><path d="M6 3v3h2" stroke="#ff8a00" stroke-width="1.4" fill="none"/></svg> 11 hours</div><hr><div class="pick">Top Insider's Pick</div><div class="from">From USD <b>$136.83</b></div><span class="deal">VIEW DEAL</span></div></article>

    <article class="card"><div class="photo" role="img" aria-label="Lit palace courtyard with pool at night" style="background:linear-gradient(180deg,#1d3a6a,#5a4a3a 55%,#c98c3a)"><svg class="heart" width="20" height="18"><path d="M10 17S0 10.5 0 5a5 5 0 0 1 10-1 5 5 0 0 1 10 1c0 5.5-10 12-10 12z" fill="#e8262a"/></svg></div><div class="body"><h2>Stonehenge, Windsor Castle, and Bath from London..</h2><div class="rating"><svg width="64" height="12"><g fill="#f5a623"><use href="#s"/><use href="#s" x="13"/><use href="#s" x="26"/><use href="#s" x="39"/><use href="#s" x="52"/></g></svg> 5042 Reviews</div><div class="meta"><svg width="9" height="12"><path d="M4.5 0a4.5 4.5 0 0 1 4.5 4.5C9 8 4.5 12 4.5 12S0 8 0 4.5A4.5 4.5 0 0 1 4.5 0z" fill="#ff8a00"/></svg> London, UK | <svg width="12" height="12"><circle cx="6" cy="6" r="5" fill="none" stroke="#ff8a00" stroke-width="1.6"/><path d="M6 3v3h2" stroke="#ff8a00" stroke-width="1.4" fill="none"/></svg> 11 hours</div><hr><div class="pick">Top Insider's Pick</div><div class="from">From USD <b>$136.83</b></div><span class="deal">VIEW DEAL</span></div></article>

    <article class="card"><div class="photo" role="img" aria-label="Resort pavilion beside a pool at dusk" style="background:linear-gradient(180deg,#2b4f8f,#3a5a8a 50%,#e0a050)"><svg class="heart" width="20" height="18"><path d="M10 17S0 10.5 0 5a5 5 0 0 1 10-1 5 5 0 0 1 10 1c0 5.5-10 12-10 12z" fill="#e8262a"/></svg></div><div class="body"><h2>Stonehenge, Windsor Castle, and Bath from London..</h2><div class="rating"><svg width="64" height="12"><g fill="#f5a623"><use href="#s"/><use href="#s" x="13"/><use href="#s" x="26"/><use href="#s" x="39"/><use href="#s" x="52"/></g></svg> 5042 Reviews</div><div class="meta"><svg width="9" height="12"><path d="M4.5 0a4.5 4.5 0 0 1 4.5 4.5C9 8 4.5 12 4.5 12S0 8 0 4.5A4.5 4.5 0 0 1 4.5 0z" fill="#ff8a00"/></svg> London, UK | <svg width="12" height="12"><circle cx="6" cy="6" r="5" fill="none" stroke="#ff8a00" stroke-width="1.6"/><path d="M6 3v3h2" stroke="#ff8a00" stroke-width="1.4" fill="none"/></svg> 11 hours</div><hr><div class="pick">Top Insider's Pick</div><div class="from">From USD <b>$136.83</b></div><span class="deal">VIEW DEAL</span></div></article>

    <article class="card"><div class="photo" role="img" aria-label="Lakeside city at twilight with hills behind" style="background:linear-gradient(180deg,#6a7fa8,#b89a8a 50%,#3a5676)"><svg class="heart" width="20" height="18"><path d="M10 17S0 10.5 0 5a5 5 0 0 1 10-1 5 5 0 0 1 10 1c0 5.5-10 12-10 12z" fill="#e8262a"/></svg></div><div class="body"><h2>Stonehenge, Windsor Castle, and Bath from London..</h2><div class="rating"><svg width="64" height="12"><g fill="#f5a623"><use href="#s"/><use href="#s" x="13"/><use href="#s" x="26"/><use href="#s" x="39"/><use href="#s" x="52"/></g></svg> 5042 Reviews</div><div class="meta"><svg width="9" height="12"><path d="M4.5 0a4.5 4.5 0 0 1 4.5 4.5C9 8 4.5 12 4.5 12S0 8 0 4.5A4.5 4.5 0 0 1 4.5 0z" fill="#ff8a00"/></svg> London, UK | <svg width="12" height="12"><circle cx="6" cy="6" r="5" fill="none" stroke="#ff8a00" stroke-width="1.6"/><path d="M6 3v3h2" stroke="#ff8a00" stroke-width="1.4" fill="none"/></svg> 11 hours</div><hr><div class="pick">Top Insider's Pick</div><div class="from">From USD <b>$136.83</b></div><span class="deal">VIEW DEAL</span></div></article>
  </div>

  <nav class="pager"><span>Prev</span><span class="on">1</span><span>2</span><span>3</span><span>4</span><span>5</span><span>6</span><span>...</span><span>22</span><span>Next</span></nav>

  <section class="panel destinations">
    <h2>Top Destinations</h2>
    <div class="arrows">
      <svg width="22" height="22"><circle cx="11" cy="11" r="11" fill="#aaa"/><path d="M13 6l-5 5 5 5" stroke="#fff" stroke-width="2.4" fill="none"/></svg>
      <svg width="22" height="22"><circle cx="11" cy="11" r="11" fill="#aaa"/><path d="M9 6l5 5-5 5" stroke="#fff" stroke-width="2.4" fill="none"/></svg>
    </div>
    <div class="dest-row">
      <div class="dest"><div class="photo" role="img" aria-label="Canal city lit at dusk" style="background:linear-gradient(180deg,#4a7ac0,#8a7a9a 55%,#2a4f7a)"></div><div class="info"><div><div class="name">Hotels London</div><div class="sub">10809 Hotels</div></div><div class="price">$175.19</div></div></div>
      <div class="dest"><div class="photo" role="img" aria-label="Coastal village above turquoise water" style="background:linear-gradient(180deg,#8fc3e6,#d9c2a8 45%,#2aa3b9)"></div><div class="info"><div><div class="name">Hotels London</div><div class="sub">10809 Hotels</div></div><div class="price">$175.19</div></div></div>
      <div class="dest"><div class="photo" role="img" aria-label="Hilltop palace over a lake" style="background:linear-gradient(180deg,#5a8fd0,#caa070 55%,#4a6a8a)"></div><div class="info"><div><div class="name">Hotels London</div><div class="sub">10809 Hotels</div></div><div class="price">$175.19</div></div></div>
    </div>
  </section>

  <section class="panel things">
    <h2>More Things to Do in London</h2>
    <ul style="left:38px"><li>Airport &amp; Ground Transfers</li><li>Attraction Tickets</li><li>Bar, Club &amp; Pub Tours</li><li>Bike &amp; Mountain Bike Tours</li><li>City Tours</li><li>Cultural Tours</li><li>Day Cruises</li></ul>
    <ul style="left:295px"><li>Day Trips</li><li>Dinner Packages</li><li>Food Tours</li><li>Full-day Tours</li><li>Half-day Tours</li><li>Hop-on Hop-off Tours</li><li>Movie &amp; TV Tours</li></ul>
    <ul style="left:519px"><li>Night Tours</li><li>Private Transfers</li><li>Rail Tours</li><li>Sightseeing &amp; City Passes</li><li>Theater, Shows &amp; Musicals</li><li>Walking Tours</li></ul>
  </section>
</main>

<footer class="site-footer">
  <div class="logo">TRIPWELL FINDER</div>
  <p class="about">At vero eos et accusamus et iusto odio dignissi mos ducimus qui blanditiis..</p>
  <div class="socials"><span></span><span></span><span></span><span></span><span></span><span></span><span></span><span></span></div>
  <div class="fsep" style="left:434px"></div>
  <div class="fcol c1"><h4>Information</h4><ul><li>About Us</li><li>Careers</li><li>Privacy &amp; Security</li><li>Site Map</li><li>Terms of Use</li><li>Blog</li></ul></div>
  <div class="fsep" style="left:620px"></div>
  <div class="fcol c2"><h4>Customer Care</h4><ul><li>Help Center</li><li>Privacy Policy</li><li>Low Price Guarantee</li><li>Group Services</li></ul></div>
  <div class="fsep" style="left:870px"></div>
  <div class="fcol c3"><h4>Resources</h4><ul><li>Work with Tripwell Finder</li><li>Supplier Sign-up</li><li>Distribution Programs</li><li>Travel Agents</li></ul></div>
  <div class="copyright">Copyright © 2017, Tripwell Finder - All Rights Reserved.</div>
</footer>

</body>
</html>
```